Indonesian B2B Company (Varo Ingredients) - Stationery Design

Varo Ingredients needs a corporate, bold and professional-looking stationery design.

Varo Ingredients is a new Indonesian company manufacturing, marketing and distributing various ingredients / raw materials such as flavours, fragrance, colours, sweeteners, preservatives for the food & beverage, pharmaceutical, personal care and other household goods industries.

It is a business to business (B2B) company as we supply various natural and synthetic raw materials to various consumer goods manufacturers. We therefore need a logo/identity with corporate and industrial style.

Varo Ingredients is a startup company which belongs to a larger Tumina Jaya group of companies (http://tuminajaya.bizplank.example/about) that focuses in the mining, petroleum and energy businesses. Varo Ingredients would like to focus in providing good quality, safe, reliable and affordable ingredients for the industries. Our tagline is "Ingredients for Your Success"
Updates

We have updated some information including our requirements and contact details to be shown in the stationery. Please check the project brief.

Regards,

Varo Ingredients

Target Market(s)

Manufacturers of food & beverages, personal care, pharmaceutical and other FMCG factories.

Industry/Entity Type

Business

Requirements
Must have
• Smart, professional and corporate touches in the stationery designs. We require designs for:
1. Letterhead
2. Envelope (with and without window)
3. Name card
4. Powerpoint presentation template
5. CD label
6. Small memo / with compliments card

Contact details:

Company name:
PT Varo Ingredients

Address:
Ruko Pelita Sumber Asri, Blok K07 no: 15-16
Cempaka Hijau Utara, 14590
Indonesia

Tel:+62 21 738 2096
Fax:+62 21 738 2097
Email: info@varo-ingredients.example
Website: www.varo-ingredients.example

```html
<!DOCTYPE html>
<html lang="en">
<head>
<meta charset="utf-8">
<title>Varo Ingredients – Stationery</title>
<link rel="stylesheet" href="https://fonts.googleapis.com/css2?family=Barlow:wght@400;500&display=swap">
<style>
  :root {
    --backdrop: #1d1d1d;
    --paper: #ffffff;
    --accent: #e3202b;
    --ink: #1a1a1a;
    --ribbon-red: #e3202b;
    --ribbon-pink: #f2485e;
    --ribbon-blue: #2f7fe6;
    --ribbon-orange: #f7a531;
    --ribbon-grey: #8c9196;
    --rule: #3a3a3a;
  }
  * { margin: 0; padding: 0; box-sizing: border-box; }
  html, body { width: 996px; height: 1200px; overflow: hidden; }
  body {
    background: var(--backdrop);
    font-family: "Barlow", "Helvetica Neue", Arial, sans-serif;
    color: var(--ink);
    position: relative;
  }
  .sheet {
    position: absolute;
    background: var(--paper);
    overflow: hidden;
  }

  /* company name */
  .company-name {
    display: flex;
    align-items: center;
    gap: 8px;
    color: var(--ink);
    font-weight: 500;
    line-height: 1;
    white-space: nowrap;
  }
  .company-name__square {
    background: var(--accent);
    flex: none;
  }
  .ribbon-band--vertical {
    position: absolute;
    background: linear-gradient(180deg,
      var(--ribbon-orange) 0%, var(--ribbon-red) 14%, var(--ribbon-blue) 28%,
      var(--ribbon-pink) 42%, var(--ribbon-grey) 56%, var(--ribbon-red) 70%,
      var(--ribbon-blue) 84%, var(--ribbon-orange) 100%);
  }
  .ribbon-band--horizontal {
    position: absolute;
    background: linear-gradient(90deg,
      var(--ribbon-orange) 0%, var(--ribbon-red) 16%, var(--ribbon-pink) 30%,
      var(--ribbon-blue) 46%, var(--ribbon-grey) 60%, var(--ribbon-red) 76%,
      var(--ribbon-blue) 90%, var(--ribbon-pink) 100%);
  }
  .contact-block { line-height: 1.3; }
  .contact-block p { white-space: nowrap; }
  .contact-block .gap { height: 1.3em; }

  /* letterhead */
  .letterhead { left: 40px; top: 40px; width: 560px; height: 792px; }
  .letterhead .ribbon-band--vertical { left: 0; top: 0; width: 40px; height: 300px; }
  .letterhead .company-name { position: absolute; left: 62px; top: 110px; font-size: 22px; }
  .letterhead .company-name__square { width: 14px; height: 14px; }
  .letterhead .contact-block { position: absolute; left: 62px; top: 150px; font-size: 10.5px; }

  /* envelope */
  .envelope { left: 40px; top: 860px; width: 620px; height: 300px; }
  .envelope .ribbon-band--vertical { left: 0; top: 0; width: 40px; height: 270px; }
  .envelope .company-name { position: absolute; left: 62px; top: 94px; font-size: 22px; }
  .envelope .company-name__square { width: 14px; height: 14px; }
  .envelope .contact-block { position: absolute; left: 62px; top: 134px; font-size: 10.5px; }
  .envelope__window-rule {
    position: absolute; right: 28px; width: 250px; height: 1px; background: var(--rule);
  }
  .envelope__window-rule--upper { top: 150px; }
  .envelope__window-rule--lower { top: 178px; }

  /* business card back */
  .card-back { left: 630px; top: 40px; width: 326px; height: 190px; }
  .card-back .company-name {
    position: absolute; left: 0; right: 0; top: 72px;
    justify-content: center; font-size: 16px;
  }
  .card-back .company-name__square { width: 10px; height: 10px; }
  .card-back .ribbon-band--horizontal { left: 0; bottom: 0; width: 100%; height: 26px; }

  /* business card front */
  .card-front { left: 630px; top: 260px; width: 326px; height: 190px; }
  .card-front .company-name { position: absolute; right: 16px; top: 20px; font-size: 13px; }
  .card-front .company-name__square { width: 8px; height: 8px; }
  .card-front .holder { position: absolute; left: 18px; top: 62px; font-size: 7.5px; font-weight: 500; line-height: 1.35; }
  .card-front .contact-block { position: absolute; left: 18px; top: 98px; font-size: 7.5px; }
  .card-front .ribbon-band--horizontal { left: 0; bottom: 20px; width: 100%; height: 22px; }
  .card-front .address-line {
    position: absolute; right: 10px; bottom: 5px; font-size: 7.5px; white-space: nowrap;
  }
</style>
</head>
<body>

  <section class="sheet letterhead" aria-label="Letterhead">
    <div class="ribbon-band--vertical" role="img" aria-label="Interlaced ribbon pattern in red, blue, orange and grey"></div>
    <div class="company-name"><span class="company-name__square"></span>Varo Ingredients</div>
    <div class="contact-block">
      <p>Ruko Pelita Sumber Asri</p>
      <p>Blok K07 no: 15-16</p>
      <p>Cempaka Hijau Utara, 14590</p>
      <p>Indonesia</p>
      <div class="gap"></div>
      <p>Tel:+62 21 738 2096</p>
      <p>Fax:+62 21 738 2097</p>
      <p>info@varo-ingredients.example</p>
      <p>www.varo-ingredients.example</p>
    </div>
  </section>

  <section class="sheet envelope" aria-label="Envelope">
    <div class="ribbon-band--vertical" role="img" aria-label="Interlaced ribbon pattern in red, blue, orange and grey"></div>
    <div class="company-name"><span class="company-name__square"></span>Varo Ingredients</div>
    <div class="contact-block">
      <p>Ruko Pelita Sumber Asri</p>
      <p>Blok K07 no: 15-16</p>
      <p>Cempaka Hijau Utara, 14590</p>
      <p>Indonesia</p>
      <div class="gap"></div>
      <p>Tel:+62 21 738 2096</p>
      <p>Fax:+62 21 738 2097</p>
      <p>info@varo-ingredients.example</p>
      <p>www.varo-ingredients.example</p>
    </div>
    <span class="envelope__window-rule envelope__window-rule--upper"></span>
    <span class="envelope__window-rule envelope__window-rule--lower"></span>
  </section>

  <section class="sheet card-back" aria-label="Business card, back">
    <div class="company-name"><span class="company-name__square"></span>Varo Ingredients</div>
    <div class="ribbon-band--horizontal" role="img" aria-label="Interlaced ribbon pattern in red, blue, orange and grey"></div>
  </section>

  <section class="sheet card-front" aria-label="Business card, front">
    <div class="company-name"><span class="company-name__square"></span>Varo Ingredients</div>
    <div class="holder">
      <p>Name</p>
      <p>Designation</p>
    </div>
    <div class="contact-block">
      <p>Tel:+62 21 738 2096</p>
      <p>Fax:+62 21 738 2097</p>
      <p>info@varo-ingredients.example</p>
      <p>www.varo-ingredients.example</p>
    </div>
    <div class="ribbon-band--horizontal" role="img" aria-label="Interlaced ribbon pattern in red, blue, orange and grey"></div>
    <p class="address-line">Ruko Pelita Sumber Asri, Blok K07 no: 15-16, Cempaka Hijau Utara, 14590 Indonesia</p>
  </section>

</body>
</html>
```